Pixagram Business Card For Comedian

Hi,

I'd like a 2-sided business card that kind mimics an Pixagram page. I've attached screenshots with the copy and language that should be written on there.

I'd like it to be way more stylized and a bit more creative than what I did on Powerpoint. I just did a mockup so that you can have an idea. I'd like it to be designed and you to take a bit of creative imagery so that it doesn't look so static and monochromatic.

PLEASE BE CREATIVE WITH THESE DESIGNS. I DON'T WANT IT TO LOOK EXACTLY LIKE THE ATTACHED IMAGE OR EXACTLY LIKE AN PIXAGRAM PAGE. I want to use it as inspiration to create something that looks more sleek, and creative. I don't want the colors to just be boring gray, and blue. Have fun and spice it up a bit!

Check out my website DanaWellmore.com to see the colors and fonts I use for my branding.

For the main photo: Here's a link with the hi-res photo: !https://www.filecrate.example/s/q8wtm3hzr5bdk2p/Dana-Wellmore-C71F2254.jpg?dl=0

For the thumbnail icon photo, you can use this: https://www.filecrate.example/s/vn4rx9kplw2tjdm/Dana%20Wellmore%20Glass%20Yard%20Headshot.jpg?dl=0

Use the Standard Business Card Template from Plinx.com:
https://help.plinx.example/hc/en-us/article_attachments/318274905/Standard_Size__US__Business_Cards_Portrait.jpg

Please let me know if you have any questions.
Updates

Industry/Entity Type

Business

Contact Information for Business Card

All of the text and copy has been provided on the attached jpg.

Colors
33a6d7
0255a3
aaaaaa
dbdbdb
1b1b1b

Requirements
Should not have
• A Hyperlink for the Email Addresses

```html
<!DOCTYPE html>
<html lang="en">
<head>
<meta charset="utf-8">
<title>Dana Wellmore – Pixagram Style Business Card</title>
<link rel="stylesheet" href="https://fonts.googleapis.com/css2?family=Kaushan+Script&family=Montserrat:wght@400;500;600;700&family=Roboto:wght@400;500;700&display=swap">
<style>
  :root {
    --sky: #33a6d7;
    --navy: #0255a3;
    --mid-grey: #aaaaaa;
    --light-grey: #dbdbdb;
    --ink: #1b1b1b;
    --panel: #232323;
    --white: #ffffff;
    --stage: #e9e9e9;
  }
  * { box-sizing: border-box; margin: 0; padding: 0; }
  html, body { width: 1200px; height: 675px; overflow: hidden; }
  body { background: var(--stage); font-family: "Montserrat", sans-serif; position: relative; }

  .card-side {
    position: absolute; top: 39px; width: 398px; height: 700px;
    transform: scale(0.857); transform-origin: top left;
    background: var(--panel); overflow: hidden;
    box-shadow: 0 6px 18px rgba(0,0,0,.25);
  }
  .card-front { left: 243px; }
  .card-back { left: 626px; }
  .abs { position: absolute; }

  /* status bar */
  .status-bar { left: 0; top: 0; width: 100%; height: 25px; background: var(--white); }
  .status-signal { left: 10px; top: 9px; font-size: 7px; letter-spacing: 1px; color: var(--ink); }
  .status-time { left: 0; width: 100%; top: 6px; text-align: center; font: 700 11px "Roboto", sans-serif; color: var(--ink); }
  .status-battery { right: 10px; top: 8px; width: 22px; height: 10px; border-radius: 2px; background: var(--ink); }

  /* tab bar */
  .tab-bar { left: 0; bottom: 0; width: 100%; height: 44px; background: var(--white); border-top: 1px solid var(--light-grey); }
  .tab-bar svg { position: absolute; top: 10px; width: 24px; height: 24px; }
  .tab-dot { width: 5px; height: 5px; border-radius: 50%; background: var(--sky); top: 36px; }

  /* front */
  .front-handle { left: 15px; top: 34px; font: 600 20px "Montserrat", sans-serif; color: var(--white); }
  .front-location { left: 15px; top: 62px; font-size: 11px; color: var(--white); }
  .front-more { right: 18px; top: 36px; font-size: 18px; color: var(--white); letter-spacing: 1px; }
  .hero-photo { left: 10px; top: 90px; width: 375px; height: 200px;
    background: linear-gradient(100deg, #e7d4c0 0%, #3a2a22 30%, #1d1612 55%, #6b4a35 75%, #e8dcc2 100%); }
  .shape-tri { position: absolute; }
  .profile-ring { left: 8px; top: 295px; width: 114px; height: 114px; border-radius: 50%; background: var(--light-grey); padding: 6px; }
  .profile-photo { width: 100%; height: 100%; border-radius: 50%; background: radial-gradient(circle at 50% 45%, #6b4a3a 0%, #2a1d17 60%, #151010 100%); }
  .name-script { font-family: "Kaushan Script", cursive; color: var(--sky); white-space: nowrap; }
  .front-name { left: 138px; top: 308px; font-size: 40px; }
  .front-roles { left: 152px; top: 366px; font: 700 16px "Montserrat", sans-serif; font-variant: small-caps; color: var(--white); letter-spacing: .5px; }
  .site-url { font: 700 11px "Montserrat", sans-serif; color: var(--sky); letter-spacing: .4px; }
  .site-url span { color: var(--white); }
  .front-url { left: 180px; top: 393px; }
  .action-icons { left: 16px; top: 435px; }
  .action-icons svg { width: 22px; height: 22px; margin-right: 9px; }
  .likes { left: 18px; top: 465px; font: 700 13px "Roboto", sans-serif; color: var(--white); }
  .view-icons { left: 303px; top: 460px; }
  .view-icons svg { width: 18px; height: 18px; margin-left: 6px; }
  .caption-area { left: 0; top: 500px; width: 100%; height: 200px; background: var(--white); }
  .caption { left: 15px; top: 513px; width: 375px; font: 400 12.2px/21px "Roboto", sans-serif; color: var(--ink); }
  .caption b { font: 700 15px "Montserrat", sans-serif; color: var(--sky); }
  .caption .more-comments { color: var(--mid-grey); font-size: 11px; }
  .notice { left: 242px; top: 622px; width: 90px; height: 24px; border-radius: 4px; background: var(--sky); color: var(--white);
    font: 500 11px/24px "Roboto", sans-serif; text-align: center; }
  .notice::after { content: ""; position: absolute; left: 38px; bottom: -7px; border: 7px solid transparent; border-bottom: 0; border-top-color: var(--sky); }

  /* back */
  .back-header { left: 0; top: 25px; width: 100%; height: 37px; background: var(--white); }
  .back-handle { left: 0; width: 100%; top: 31px; text-align: center; font: 600 22px "Montserrat", sans-serif; color: var(--ink); }
  .gear { right: 12px; top: 32px; width: 22px; height: 22px; }
  .portrait-photo { left: 36px; top: 62px; width: 323px; height: 258px;
    background: radial-gradient(ellipse at 50% 40%, #6e4b3b 0%, #2a1c16 45%, #1a1210 70%, #c9655a 100%); }
  .side-tag { top: 170px; width: 190px; font: 600 12px "Montserrat", sans-serif; color: var(--white); letter-spacing: 1.2px; text-align: center; white-space: nowrap; }
  .side-tag-left { left: -77px; transform: rotate(-90deg); }
  .side-tag-right { right: -77px; transform: rotate(90deg); }
  .stat { text-align: center; width: 90px; }
  .stat strong { display: block; font: 700 18px "Roboto", sans-serif; color: var(--white); }
  .stat span { font: 400 15px "Roboto", sans-serif; color: var(--mid-grey); }
  .stat-posts { left: 16px; top: 340px; }
  .stat-followers { left: 286px; top: 340px; }
  .back-name { left: 0; width: 100%; top: 325px; text-align: center; font-size: 31px; }
  .back-url { left: 0; width: 100%; top: 370px; text-align: center; font-size: 10px; }
  .edit-button { left: 30px; top: 392px; width: 333px; height: 36px; border-radius: 3px; background: #f0f0f0;
    font: 700 18px/36px "Roboto", sans-serif; color: var(--ink); text-align: center; }
  .block-title { left: 30px; font: 500 16px "Montserrat", sans-serif; color: var(--sky); }
  .block-text { left: 30px; width: 350px; font: 400 12.3px/17px "Montserrat", sans-serif; color: var(--white); }
  .label { font-variant: small-caps; }
  .seen-on { left: 0; width: 100%; top: 604px; text-align: center; font: 700 10.5px "Montserrat", sans-serif; color: var(--white); }
  .seen-on span { color: var(--sky); }
  .socials { left: 0; width: 100%; top: 634px; display: flex; justify-content: center; gap: 14px; font: 500 12px "Montserrat", sans-serif; color: var(--white); }
  .socials i { display: inline-block; width: 11px; height: 11px; border-radius: 50%; background: var(--sky); margin-right: 6px; vertical-align: -1px; }
</style>
</head>
<body>

<!-- FRONT -->
<section class="card-side card-front">
  <div class="abs status-bar">
    <span class="abs status-signal">●●●●●</span>
    <div class="abs status-time">04:20</div>
    <span class="abs status-battery"></span>
  </div>
  <div class="abs front-handle">hivelane</div>
  <div class="abs front-location">Brooklyn, New York</div>
  <div class="abs front-more">•••</div>

  <div class="abs hero-photo" role="img" aria-label="Photo of the comedian holding her hands to her face, wearing large gold rings"></div>
  <svg class="shape-tri" style="left:0;top:118px" width="60" height="124" viewBox="0 0 60 124"><polygon points="0,0 58,62 0,124" fill="var(--sky)"/></svg>
  <svg class="shape-tri" style="left:330px;top:120px" width="68" height="126" viewBox="0 0 68 126"><polygon points="68,0 0,63 68,126" fill="var(--sky)"/></svg>

  <div class="abs profile-ring"><div class="profile-photo" role="img" aria-label="Headshot thumbnail of the comedian"></div></div>
  <div class="abs name-script front-name">Dana Wellmore</div>
  <div class="abs front-roles">Comedian | Actor | Writer</div>
  <div class="abs site-url front-url">WWW.DANAWELLMORE<span>.COM</span></div>

  <div class="abs action-icons">
    <svg viewBox="0 0 24 24" fill="none" stroke="#fff" stroke-width="1.6"><path d="M12 20s-7-4.5-7-10a4 4 0 0 1 7-2.5A4 4 0 0 1 19 10c0 5.5-7 10-7 10z"/></svg>
    <svg viewBox="0 0 24 24" fill="none" stroke="#fff" stroke-width="1.6"><path d="M20 12a8 8 0 1 1-3.5-6.6A8 8 0 0 1 20 12zm0 0l1 7-5-2"/></svg>
    <svg viewBox="0 0 24 24" fill="none" stroke="#fff" stroke-width="1.6"><path d="M4 20v-4a6 6 0 0 1 6-6h10m-5-5l5 5-5 5"/></svg>
  </div>
  <div class="abs likes">♥ 321 likes</div>
  <div class="abs view-icons">
    <svg viewBox="0 0 18 18" fill="var(--sky)"><rect x="1" y="1" width="4" height="4"/><rect x="7" y="1" width="4" height="4"/><rect x="13" y="1" width="4" height="4"/><rect x="1" y="7" width="4" height="4"/><rect x="7" y="7" width="4" height="4"/><rect x="13" y="7" width="4" height="4"/><rect x="1" y="13" width="4" height="4"/><rect x="7" y="13" width="4" height="4"/><rect x="13" y="13" width="4" height="4"/></svg>
    <svg viewBox="0 0 18 18" stroke="var(--sky)" stroke-width="1.5"><path d="M1 3h16M1 9h16M1 15h16"/></svg>
    <svg viewBox="0 0 18 18" fill="none" stroke="var(--sky)" stroke-width="1.5"><path d="M9 17s-5-5.5-5-9a5 5 0 0 1 10 0c0 3.5-5 9-5 9z"/><circle cx="9" cy="8" r="2"/></svg>
  </div>

  <div class="abs caption-area"></div>
  <p class="abs caption"><b>hivelane</b> Your favorite comic's favorite comic. #ISAIDIT #SOITSTRUE #FINDME #FOLLOWME #NOTTOMYHOUSE #POSTABOUTMEUSINGTHESEHASHTAGS #DANAWELLMORE #HIVELANE #IMSUCHABROOKLYNGIRL #MAKENYUNSAFEAGAIN #BROOKLYNSTANDUPCOMEDY<br><span class="more-comments">view all 12 comments</span></p>
  <div class="abs notice">● 3 ♥ 2 ▲ 1</div>

  <nav class="abs tab-bar">
    <svg style="left:7px" viewBox="0 0 24 24" fill="var(--ink)"><path d="M3 11l9-8 9 8v10h-6v-6H9v6H3z"/></svg>
    <svg style="left:96px" viewBox="0 0 24 24" fill="none" stroke="#777" stroke-width="1.6"><circle cx="10" cy="10" r="7"/><path d="M15 15l6 6"/></svg>
    <svg style="left:186px" viewBox="0 0 24 24" fill="none" stroke="#777" stroke-width="1.6"><rect x="2" y="6" width="20" height="15" rx="2"/><circle cx="12" cy="13" r="4"/><path d="M8 6l2-3h4l2 3"/></svg>
    <svg style="left:275px" viewBox="0 0 24 24" fill="none" stroke="#777" stroke-width="1.6"><path d="M12 20s-8-5-8-11a4.5 4.5 0 0 1 8-2.5A4.5 4.5 0 0 1 20 9c0 6-8 11-8 11z"/></svg>
    <span class="abs tab-dot" style="left:284px"></span>
    <svg style="left:364px" viewBox="0 0 24 24" fill="none" stroke="#777" stroke-width="1.6"><circle cx="12" cy="8" r="4.5"/><path d="M3 22a9 9 0 0 1 18 0"/></svg>
  </nav>
</section>

<!-- BACK -->
<section class="card-side card-back">
  <div class="abs status-bar">
    <span class="abs status-signal">●●●●●</span>
    <div class="abs status-time">04:20</div>
    <span class="abs status-battery"></span>
  </div>
  <div class="abs back-header"></div>
  <div class="abs back-handle">hivelane</div>
  <svg class="abs gear" viewBox="0 0 24 24" fill="none" stroke="var(--ink)" stroke-width="2"><circle cx="12" cy="12" r="4"/><path d="M12 1v4M12 19v4M1 12h4M19 12h4M4.2 4.2l2.8 2.8M17 17l2.8 2.8M4.2 19.8L7 17M17 7l2.8-2.8"/></svg>

  <div class="abs portrait-photo" role="img" aria-label="Portrait photo of the comedian with voluminous curly hair, coral top"></div>
  <div class="abs side-tag side-tag-left">LET'S STAY CONNECTED!</div>
  <div class="abs side-tag side-tag-right">LET'S STAY CONNECTED!</div>
  <svg class="shape-tri" style="left:0;top:265px" width="45" height="60" viewBox="0 0 45 60"><polygon points="0,0 44,30 0,60" fill="var(--sky)"/></svg>
  <svg class="shape-tri" style="left:355px;top:265px" width="43" height="60" viewBox="0 0 43 60"><polygon points="43,0 0,30 43,60" fill="var(--sky)"/></svg>

  <div class="abs stat stat-posts"><strong>3431</strong><span>posts</span></div>
  <div class="abs stat stat-followers"><strong>10K</strong><span>followers</span></div>
  <div class="abs name-script back-name">Dana Wellmore</div>
  <div class="abs site-url back-url">WWW.DANAWELLMORE<span>.COM</span></div>
  <div class="abs edit-button">Edit Profile</div>

  <h2 class="abs block-title" style="top:442px">ABOUT ME</h2>
  <p class="abs block-text" style="top:462px">Stand Up Comedian. I Host. I Write. I Act. I Dance. I Do Not Sing Unless I'm in the Shower. I Accept Tips. (Not on Jokes, but on Payvo.)</p>

  <h2 class="abs block-title" style="top:527px">BOOK ME</h2>
  <p class="abs block-text" style="top:547px"><span class="label">Management:</span> Mira@NorthgateTalent.com<br><span class="label">Agent:</span> Joan.Pell@brightdesk.com</p>

  <p class="abs seen-on">AS SEEN <span>ON KDX</span>, <span>LAUGH CHANNEL</span>, <span>TUNEWAVE</span>, <span>TRUELINE TV</span>, <span>EDGEWIRE</span>, AND <span>CREST TV</span>.</p>
  <div class="abs socials">
    <span><i></i>DANAWELLMORE</span>
    <span><i></i>HIVELANE</span>
    <span><i></i>HIVELANE</span>
  </div>

  <nav class="abs tab-bar">
    <svg style="left:7px" viewBox="0 0 24 24" fill="none" stroke="#777" stroke-width="1.6"><path d="M3 11l9-8 9 8v10h-6v-6H9v6H3z"/></svg>
    <svg style="left:96px" viewBox="0 0 24 24" fill="none" stroke="#777" stroke-width="1.6"><circle cx="10" cy="10" r="7"/><path d="M15 15l6 6"/></svg>
    <svg style="left:186px" viewBox="0 0 24 24" fill="none" stroke="#777" stroke-width="1.6"><rect x="2" y="6" width="20" height="15" rx="2"/><circle cx="12" cy="13" r="4"/><path d="M8 6l2-3h4l2 3"/></svg>
    <svg style="left:275px" viewBox="0 0 24 24" fill="none" stroke="#777" stroke-width="1.6"><path d="M12 20s-8-5-8-11a4.5 4.5 0 0 1 8-2.5A4.5 4.5 0 0 1 20 9c0 6-8 11-8 11z"/></svg>
    <span class="abs tab-dot" style="left:284px"></span>
    <svg style="left:364px" viewBox="0 0 24 24" fill="var(--ink)"><circle cx="12" cy="8" r="4.5"/><path d="M3 22a9 9 0 0 1 18 0z"/></svg>
  </nav>
</section>

</body>
</html>
```